Manuka honey wholesales and exports

We need business cards for our honey distribution company based in New Zealand. We supply shops locally and export Manuka honey around the world.
We deal with a very high quality and 100% natural product that can be used for medical, general health as well as food. We are looking business cards that show our honey products are of a high quality with a modern look.

Target Market(s)

Health and medical retailers and importers

Industry/Entity Type

Wholesale

Contact Information for Business Card

Tevin Apiary NZ Limited

www.tevinapiarynz.example

Derek Fawley

M +64 219036482

E tevinapiarynz@mailbox.example

PO Box 58-214
Takapuna
North Shore
Auckland
New Zealand

Font styles to use
Serif

Requirements
Must have
• (Tevin Apiary NZ Limited) with some artwork on one side and all details on the other side.
Nice to have
• I have seen a very simple card with large yellow and black stripes on one side with a company name.. looked clean and simple so something similar or just let the creative beast inside you take over and we will see what you can come up with.

```html
<!DOCTYPE html>
<html lang="en">
<head>
<meta charset="utf-8">
<title>Tevin Apiary – Business Card</title>
<link rel="stylesheet" href="https://fonts.googleapis.com/css2?family=Ubuntu:wght@400;500;700&display=swap">
<style>
  :root {
    --backdrop: #e8e8e8;
    --honey-light: #f6b038;
    --honey-deep: #e9a02b;
    --brown: #4a1d0c;
    --honey-faint: rgba(210, 140, 30, 0.28);
  }
  * { margin: 0; padding: 0; box-sizing: border-box; }
  html, body {
    width: 1200px; height: 576px; overflow: hidden;
    background: var(--backdrop);
    font-family: "Ubuntu", sans-serif;
    color: var(--brown);
  }
  .canvas { position: relative; width: 1200px; height: 576px; }
  .card {
    position: absolute;
    border-radius: 13px;
    background: linear-gradient(180deg, var(--honey-light) 0%, var(--honey-deep) 100%);
    overflow: hidden;
  }
  .card--front { left: 82px; top: 139px; width: 484px; height: 293px; }
  .card--back  { left: 603px; top: 138px; width: 480px; height: 291px; }

  .comb-decoration {
    position: absolute; left: 282px; top: 6px; width: 196px; height: 280px;
    border-radius: 12px;
    background: linear-gradient(180deg, var(--honey-faint), rgba(210,140,30,0.12));
  }

  .brand { position: absolute; text-align: center; }
  .brand__square {
    display: block; margin: 0 auto 10px;
    width: 52px; height: 52px; border-radius: 4px;
    background: var(--brown);
  }
  .brand__name {
    display: block; font-weight: 500; font-size: 29px; line-height: 1;
    letter-spacing: -0.3px; white-space: nowrap;
  }
  .card--front .brand { left: 36px; top: 104px; width: 190px; }
  .card--back .brand  { left: 140px; top: 110px; width: 200px; }
  .card--back .brand__square { width: 56px; height: 56px; }
  .card--back .brand__name { font-size: 31px; }

  .details { position: absolute; left: 267px; top: 74px; }
  .details__name { font-weight: 700; font-size: 21px; letter-spacing: -0.2px; margin-bottom: 18px; }
  .details__address { font-size: 12.5px; line-height: 16px; margin-bottom: 14px; }
  .contact-list { list-style: none; font-size: 12.5px; }
  .contact-list li { display: flex; align-items: center; height: 17px; }
  .contact-list svg { width: 11px; height: 11px; margin-right: 13px; flex: none; fill: var(--brown); }
</style>
</head>
<body>
<main class="canvas">
  <section class="card card--front" aria-label="Business card front">
    <div class="comb-decoration" role="img" aria-label="Faint honeycomb stripe decoration"></div>
    <div class="brand">
      <span class="brand__square"></span>
      <span class="brand__name">Tevin Apiary</span>
    </div>
    <div class="details">
      <p class="details__name">Derek Fawley</p>
      <p class="details__address">PO Box 58-214 Takapuna<br>North Shore Auckland NZ</p>
      <ul class="contact-list">
        <li>
          <svg viewBox="0 0 12 12" aria-hidden="true"><path d="M3 0h6a1 1 0 0 1 1 1v10a1 1 0 0 1-1 1H3a1 1 0 0 1-1-1V1a1 1 0 0 1 1-1zm.5 1.5v7.5h5V1.5z"/></svg>
          +64 219036482
        </li>
        <li>
          <svg viewBox="0 0 12 12" aria-hidden="true"><path d="M0 2h12v8H0zm1 1.2v.3l5 3.2 5-3.2v-.3z"/></svg>
          tevinapiarynz@mailbox.example
        </li>
        <li>
          <svg viewBox="0 0 12 12" aria-hidden="true"><path d="M6 0a6 6 0 1 0 0 12A6 6 0 0 0 6 0zm-.6 1.1v2.3H3.3A5 5 0 0 1 5.4 1.1zm1.2 0a5 5 0 0 1 2.1 2.3H6.6zM1.6 4.6h3.8v2.8H1.6a5 5 0 0 1 0-2.8zm5 0h3.8a5 5 0 0 1 0 2.8H6.6zM3.3 8.6h2.1v2.3a5 5 0 0 1-2.1-2.3zm3.3 0h2.1a5 5 0 0 1-2.1 2.3z"/></svg>
          www.tevinapiarynz.example
        </li>
      </ul>
    </div>
  </section>

  <section class="card card--back" aria-label="Business card back">
    <div class="brand">
      <span class="brand__square"></span>
      <span class="brand__name">Tevin Apiary</span>
    </div>
  </section>
</main>
</body>
</html>
```